****Business Card Design for Cormwell Development. Design based around attached logo/company name

I’m looking for business card design for my company Cormwell Development Group,LLC. Design should be professional, sharp and minimal. Outside of the attached logos, greyscale colors for remainder of cards. My thoughts are two-sided card with attached logo on one side and my info on the other but open to one-sided as well with right design.
Target Market(s)
Real estate professionals including banks, private investors, property owners, developers, commercial tenants like Brewlantic, Granvey or Tamsett’s.
Industry/Entity Type
Commercial real estate development and investments.
Contact Information for Business Card
Name, title, email, phone #’s, web address and physical address
Font styles to use
Other font styles liked:
- Helvetica, Garamond, etc
Colors
Designer to choose only greyscale colors for use in the design.
Requirements
Must have
- Attached logo first or second options.
Nice to have
- Two sided card with logo on one side. Attached Logo/company name can be laid out any way that flows as long as it’s legible.name
Should not have
- No loud colors. ***Please do not include logo, I have removed the company design with a logo image.

```html
<!DOCTYPE html>
<html lang="en">
<head>
<meta charset="utf-8">
<title>Cormwell Development Group – Business Card</title>
<link rel="stylesheet" href="https://fonts.googleapis.com/css2?family=Cormorant+Garamond:wght@700&family=Arimo:wght@400&display=swap">
<style>
  :root {
    --backdrop: #eceded;
    --card: #5b6577;
    --ink-light: #e4e6ea;
    --ink-soft: #c9ced6;
    --accent-block: #d7d9de;
  }
  * { box-sizing: border-box; margin: 0; padding: 0; }
  html, body { width: 1200px; height: 900px; overflow: hidden; }
  body {
    background: var(--backdrop);
    position: relative;
    font-family: "Arimo", Helvetica, Arial, sans-serif;
  }
  .card {
    position: absolute;
    left: 250px;
    width: 700px;
    height: 400px;
    background: var(--card);
    box-shadow: 0 4px 14px rgba(0,0,0,0.12);
  }
  .card--front { top: 40px; }
  .card--back { top: 460px; }

  .company-name {
    position: absolute;
    font-family: "Arimo", Helvetica, Arial, sans-serif;
    font-weight: 400;
    color: var(--ink-light);
    white-space: nowrap;
  }
  .card--front .company-name {
    left: 0; right: 0; top: 150px;
    text-align: center;
    font-size: 34px;
  }
  .card--back .company-name {
    right: 50px; top: 52px;
    text-align: right;
    font-size: 20px;
  }

  .contact {
    position: absolute;
    left: 40px;
    bottom: 38px;
    display: flex;
    gap: 18px;
    color: var(--ink-light);
  }
  .contact__marker {
    width: 18px;
    height: 34px;
    background: var(--accent-block);
    margin-top: 14px;
  }
  .contact__name {
    font-family: "Cormorant Garamond", Garamond, serif;
    font-weight: 700;
    font-size: 22px;
    letter-spacing: 1.5px;
    text-transform: uppercase;
  }
  .contact__title, .contact__address, .contact__line {
    font-size: 15px;
    line-height: 1.3;
    color: var(--ink-soft);
  }
  .contact__address { margin-top: 14px; }
  .contact__lines { margin-top: 14px; list-style: none; }
  .contact__line { display: flex; align-items: center; gap: 8px; margin-top: 3px; }
  .contact__line svg { width: 13px; height: 13px; flex: none; }
</style>
</head>
<body>
  <section class="card card--front">
    <p class="company-name">Cormwell Development Group, LLC</p>
  </section>

  <section class="card card--back">
    <p class="company-name">Cormwell Development Group, LLC</p>

    <div class="contact">
      <div class="contact__marker"></div>
      <div class="contact__body">
        <p class="contact__name">Daniel Ashcombe</p>
        <p class="contact__title">Founder/CEO</p>
        <p class="contact__address">2190 Harbor Point Drive<br>Lakeview AB 5263</p>
        <ul class="contact__lines">
          <li class="contact__line">
            <svg viewBox="0 0 16 16" aria-hidden="true"><circle cx="8" cy="8" r="8" fill="#c9ced6"/><path d="M5 4.5l1.6-.3.9 2-1 .8a5 5 0 0 0 2.5 2.5l.8-1 2 .9-.3 1.6c-3.6.3-6.8-2.9-6.5-6.5z" fill="#5b6577"/></svg>
            (555)-312-0496
          </li>
          <li class="contact__line">
            <svg viewBox="0 0 16 16" aria-hidden="true"><rect x="1" y="3.5" width="14" height="9" rx="1" fill="#c9ced6"/><path d="M1.5 4l6.5 5 6.5-5" fill="none" stroke="#5b6577" stroke-width="1.2"/></svg>
            info@cormwelldevelopment.com
          </li>
          <li class="contact__line">
            <svg viewBox="0 0 16 16" aria-hidden="true"><circle cx="8" cy="8" r="7" fill="#c9ced6"/><path d="M1 8h14M8 1c-3 3.5-3 10.5 0 14M8 1c3 3.5 3 10.5 0 14" fill="none" stroke="#5b6577" stroke-width="1"/></svg>
            www.cormwelldevelopment.com
          </li>
        </ul>
      </div>
    </div>
  </section>
</body>
</html>
```